International Company needs a Letterhead & Envelope Design

Our Company name is Corvale Brightwick Limited.
We'd like to ask the Designers for the luxurious and sophisticated design. Our logo is very simple and neat with letter logos, so we look forward to more professional and refined designs from Designers.
We look forward to providing you with a great design.
Thanks very much in advance.

```html
<!DOCTYPE html>
<html lang="en">
<head>
<meta charset="utf-8">
<title>Corvale Brightwick Limited — Letterhead</title>
<link href="https://fonts.googleapis.com/css2?family=Montserrat:wght@400;500;800&display=swap" rel="stylesheet">
<style>
  :root {
    --backdrop: #e9e6e2;
    --paper: #ffffff;
    --ink: #3a3a3c;
    --ink-soft: #6b6b6e;
    --rule: #4a4a4d;
  }
  * { margin: 0; padding: 0; box-sizing: border-box; }
  html, body {
    width: 1200px; height: 857px; overflow: hidden;
    background: var(--backdrop);
    font-family: "Montserrat", Arial, sans-serif;
    color: var(--ink);
  }
  .letterhead {
    position: absolute; left: 320px; top: 38px;
    width: 560px; height: 781px;
    background: var(--paper);
    box-shadow: 0 6px 18px rgba(0,0,0,.18);
  }
  .rule-top {
    position: absolute; left: 0; top: 34px; width: 100%; height: 4px;
    background: var(--rule);
  }
  .rule-bottom {
    position: absolute; left: 0; bottom: 34px; width: 100%; height: 4px;
    background: var(--rule);
  }
  .brand {
    position: absolute; background: var(--paper);
    font-weight: 800; font-size: 30px; letter-spacing: 1px;
    color: var(--ink); line-height: 1; padding: 0 12px;
  }
  .brand--top { left: 18px; top: 22px; }
  .brand--bottom { right: 18px; bottom: 22px; }
  .contact {
    position: absolute; left: 338px; top: 60px;
    list-style: none; font-size: 9px; color: var(--ink-soft);
  }
  .contact li { display: flex; align-items: center; gap: 8px; height: 20px; }
  .contact svg { width: 13px; height: 13px; }
  .letter-body {
    position: absolute; left: 150px; top: 175px; width: 280px;
    font-size: 9px; line-height: 1.45; text-align: justify; color: var(--ink);
  }
  .letter-body p { margin-bottom: 22px; }
  .sign-off {
    position: absolute; left: 420px; top: 640px;
    font-size: 8.5px; line-height: 1.5; color: var(--ink-soft);
  }
</style>
</head>
<body>
  <main class="letterhead">
    <div class="rule-top"></div>
    <div class="brand brand--top">CORVALE</div>

    <ul class="contact">
      <li>
        <svg viewBox="0 0 14 14"><circle cx="7" cy="7" r="6.2" fill="none" stroke="#4a4a4d" stroke-width="1"/><path d="M5 4.2l1.2 1.4-.6.8a4 4 0 0 0 2 2l.8-.6 1.4 1.2-.7.9c-2.4 0-4.8-2.4-4.8-4.8z" fill="#4a4a4d"/></svg>
        <span>0123 456 789</span>
      </li>
      <li>
        <svg viewBox="0 0 14 14"><circle cx="7" cy="7" r="6.2" fill="none" stroke="#4a4a4d" stroke-width="1"/><rect x="4" y="5" width="6" height="4.2" fill="none" stroke="#4a4a4d" stroke-width=".8"/><path d="M4 5l3 2.3L10 5" fill="none" stroke="#4a4a4d" stroke-width=".8"/></svg>
        <span>hello@corvale.example</span>
      </li>
      <li>
        <svg viewBox="0 0 14 14"><circle cx="7" cy="7" r="6.2" fill="none" stroke="#4a4a4d" stroke-width="1"/><path d="M7 10.4S4.7 7.8 4.7 6.2a2.3 2.3 0 0 1 4.6 0C9.3 7.8 7 10.4 7 10.4z" fill="#4a4a4d"/><circle cx="7" cy="6.2" r=".8" fill="#fff"/></svg>
        <span>12 Harbor Row</span>
      </li>
    </ul>

    <section class="letter-body">
      <p>Dear reader, thank you for your continued trust in our team. This letter outlines the next steps of our shared project and the schedule we have agreed for the coming months.</p>
      <p>Our designers will prepare the first drafts within two weeks, and we will share them with you for review. Your comments will guide every revision until the work is complete.</p>
      <p>We also propose a short meeting at your office to confirm details, budget and delivery dates. Please let us know which day suits you best.</p>
      <p>All printed materials will follow the agreed colour palette and paper stock, ensuring a consistent and refined look across every item.</p>
      <p>Should you have any questions, our team is available by phone or email during regular business hours.</p>
    </section>

    <div class="sign-off">
      <p>Yours sincerely,</p>
      <p>Marten Holloway</p>
    </div>

    <div class="rule-bottom"></div>
    <div class="brand brand--bottom">CORVALE</div>
  </main>
</body>
</html>
```